I already have a logo created by Quillory Makers that I'm very happy with. I need to spruce up my business card now. Its a double sided card with not much info on it, I like to keep it simple.
Front of card: name, phone # email address, web address. Tag Line "Outsourced Technology Solutions", under that it says Business Voice Services & Electronic Protection.
Rear of Card: Content written inside a "cloud" saying "Cloud Solutions" "Cloud Integrity"

Target Market(s)

Business to Business

Industry/Entity Type

Business

Contact Information for Business Card

We are in the technology field. Providing Telephone systems (hardware), SIP Trunks (dial tone/local/long distance/telephone #'s), LAN (Local Area Network)infrastructure cabling, Data Center solutions and Security Applications (Camera systems, Access Control systems,

Requirements
Must have
• Must have brevity
Should not have
• Clutter and/or too much information

```html
<!DOCTYPE html>
<html lang="en">
<head>
<meta charset="utf-8">
<title>Northvale Signal Works – Business Card</title>
<link rel="stylesheet" href="https://fonts.googleapis.com/css2?family=Open+Sans:wght@400;600&family=Raleway:wght@400;500&display=swap">
<style>
  :root {
    --navy: #0d3f7f;
    --slate: #7d7d7f;
    --white: #ffffff;
    --ink-grey: #6b6b6e;
    --backdrop: #eceae7;
  }
  * { margin: 0; padding: 0; box-sizing: border-box; }
  html, body { width: 1200px; height: 900px; overflow: hidden; }
  body {
    position: relative;
    background: var(--backdrop);
    font-family: "Open Sans", Arial, sans-serif;
  }
  .card {
    position: absolute;
    overflow: hidden;
    box-shadow: 0 4px 14px rgba(0,0,0,0.18);
  }

  /* Front */
  .card-front {
    left: 238px; top: 62px; width: 555px; height: 343px;
    background: var(--navy);
    color: var(--white);
  }
  .card-front .shapes { position: absolute; inset: 0; }
  .holder { position: absolute; left: 24px; top: 72px; }
  .holder-name { font-size: 19px; font-weight: 600; line-height: 1.2; }
  .holder-title { font-size: 14.5px; line-height: 1.2; }
  .contact-list {
    position: absolute; right: 28px; top: 62px;
    list-style: none; text-align: right;
    font-size: 14.5px; line-height: 20.5px;
  }
  .contact-list li { display: flex; justify-content: flex-end; align-items: center; gap: 6px; }
  .contact-list svg { width: 11px; height: 11px; fill: var(--white); }
  .front-tagline {
    position: absolute; right: 22px; top: 194px;
    font-size: 17px;
  }
  .front-services {
    position: absolute; right: 20px; top: 280px;
    font-size: 14.5px; line-height: 20px; text-align: right;
  }

  /* Back */
  .card-back {
    left: 457px; top: 518px; width: 560px; height: 344px;
    background: var(--white);
  }
  .brand {
    position: absolute; left: 90px; top: 38px; width: 390px;
    display: flex; align-items: center; gap: 10px;
  }
  .brand-mark { width: 22px; height: 22px; background: var(--navy); flex: none; }
  .brand-name {
    font-family: "Raleway", "Open Sans", sans-serif;
    font-weight: 500; font-size: 25px; line-height: 1.05;
    color: var(--navy);
  }
  .brand-rule {
    position: absolute; left: 122px; top: 120px; width: 312px;
    height: 2px; background: var(--slate);
  }
  .back-tagline {
    position: absolute; left: 121px; top: 124px;
    font-family: "Raleway", "Open Sans", sans-serif;
    font-size: 19px; color: var(--ink-grey);
  }
  .cloud { position: absolute; top: 190px; width: 260px; height: 130px; }
  .cloud svg { position: absolute; inset: 0; }
  .cloud-label {
    position: absolute; left: 0; right: 0; top: 44px;
    text-align: center; color: var(--white);
    font-size: 18.5px; line-height: 25px;
  }
  .cloud-solutions { left: 18px; }
  .cloud-integrity { left: 284px; }
</style>
</head>
<body>

<section class="card card-front" aria-label="Business card front">
  <svg class="shapes" viewBox="0 0 555 343" aria-hidden="true">
    <rect x="0" y="171" width="555" height="8" fill="#7d7d7f"/>
    <polygon points="0,183 375,252 323,343 0,343" fill="#7d7d7f"/>
  </svg>
  <div class="holder">
    <p class="holder-name">Adrian Pell</p>
    <p class="holder-title">Managing Director</p>
  </div>
  <ul class="contact-list">
    <li>044-987 654 321
      <svg viewBox="0 0 24 24"><path d="M6.6 10.8a15 15 0 0 0 6.6 6.6l2.2-2.2c.3-.3.7-.4 1-.2 1.1.4 2.3.6 3.6.6.6 0 1 .4 1 1V20c0 .6-.4 1-1 1A17 17 0 0 1 3 4c0-.6.4-1 1-1h3.5c.6 0 1 .4 1 1 0 1.3.2 2.5.6 3.6.1.3 0 .7-.2 1z"/></svg>
    </li>
    <li>hello@northvalesignal.com
      <svg viewBox="0 0 24 24"><path d="M2 5h20v14H2z M3 6l9 7 9-7" stroke="#0d3f7f" stroke-width="1.5"/></svg>
    </li>
    <li>www.northvalesignal.com
      <svg viewBox="0 0 24 24"><circle cx="12" cy="12" r="10"/><path d="M2 12h20M12 2c3 3 3 17 0 20M12 2c-3 3-3 17 0 20" stroke="#0d3f7f" stroke-width="1.5" fill="none"/></svg>
    </li>
  </ul>
  <p class="front-tagline">Outsourced Technology Solutions</p>
  <p class="front-services">Business Voice Services<br>&amp; Electronic Protection</p>
</section>

<section class="card card-back" aria-label="Business card back">
  <div class="brand">
    <span class="brand-mark" aria-hidden="true"></span>
    <p class="brand-name">Northvale Signal Works, LLC</p>
  </div>
  <div class="brand-rule"></div>
  <p class="back-tagline">Outsourced Technology Solutions</p>

  <div class="cloud cloud-solutions">
    <svg viewBox="0 0 260 130" aria-hidden="true">
      <path d="M50 124 C20 124 2 108 6 92 C10 76 32 70 52 74 C52 58 60 50 74 48 C76 20 100 4 130 4 C160 4 184 20 186 48 C202 50 210 60 208 74 C230 70 252 78 254 94 C256 110 238 124 210 124 Z" fill="#0d3f7f" transform="translate(3,3)" opacity="0.25"/>
      <path d="M50 124 C20 124 2 108 6 92 C10 76 32 70 52 74 C52 58 60 50 74 48 C76 20 100 4 130 4 C160 4 184 20 186 48 C202 50 210 60 208 74 C230 70 252 78 254 94 C256 110 238 124 210 124 Z" fill="#0d3f7f"/>
    </svg>
    <p class="cloud-label">Cloud<br>Solutions</p>
  </div>

  <div class="cloud cloud-integrity">
    <svg viewBox="0 0 260 130" aria-hidden="true">
      <path d="M50 124 C20 124 2 108 6 92 C10 76 32 70 52 74 C52 58 60 50 74 48 C76 20 100 4 130 4 C160 4 184 20 186 48 C202 50 210 60 208 74 C230 70 252 78 254 94 C256 110 238 124 210 124 Z" fill="#0d3f7f" transform="translate(3,3)" opacity="0.25"/>
      <path d="M50 124 C20 124 2 108 6 92 C10 76 32 70 52 74 C52 58 60 50 74 48 C76 20 100 4 130 4 C160 4 184 20 186 48 C202 50 210 60 208 74 C230 70 252 78 254 94 C256 110 238 124 210 124 Z" fill="#0d3f7f"/>
    </svg>
    <p class="cloud-label">Cloud<br>Integrity</p>
  </div>
</section>

</body>
</html>
```